Business Card Design using new attached logo

We are a family run Plumbing and Heating firm looking to improve our company image with an improved business card and new logo.We are looking to keep the company colour (Blue) involved in our design

Reason: New logo added which needs to be incorporated on designs

Industry/Entity Type

Business

Contact Information for Business Card

See attachment of all info required.

Requirements
Must have
• We have just picked a new company logo which is attached.
• Could you please provide your business card designs using this logo.
• We are looking for the logo on the back as well as the front with all the info required

```html
<!DOCTYPE html>
<html lang="en">
<head>
<meta charset="utf-8">
<title>KVL Services Ltd – Business Card</title>
<link rel="stylesheet" href="https://fonts.googleapis.com/css2?family=Marcellus+SC&display=swap">
<style>
  :root {
    --brand-blue: #3b63b2;
    --tree-tint: #bcc5e8;
    --tree-tint-soft: #e3e7f6;
    --paper: #ffffff;
  }
  * { margin: 0; padding: 0; box-sizing: border-box; }
  html, body {
    width: 1200px;
    height: 791px;
    overflow: hidden;
    background: var(--paper);
  }
  .business-card {
    position: relative;
    width: 1200px;
    height: 791px;
    background: var(--paper);
    font-family: "Marcellus SC", serif;
    color: var(--brand-blue);
    overflow: hidden;
  }
  .tree-artwork {
    position: absolute;
    left: 200px;
    top: 140px;
    width: 1000px;
    height: 651px;
  }
  .brand-name,
  .brand-suffix {
    position: absolute;
    top: 98px;
    height: 601px;
    writing-mode: vertical-rl;
    transform: rotate(180deg);
    white-space: nowrap;
    font-weight: 400;
    color: var(--brand-blue);
  }
  .brand-name {
    left: 28px;
    width: 140px;
    font-size: 178px;
    line-height: 140px;
    letter-spacing: 4px;
  }
  .brand-suffix {
    left: 170px;
    width: 52px;
    font-size: 58px;
    line-height: 52px;
    letter-spacing: 7px;
  }
  .address {
    position: absolute;
    right: 80px;
    top: 340px;
    text-align: right;
    font-size: 41px;
    line-height: 52px;
    letter-spacing: 2px;
    text-transform: lowercase;
  }
  .contact-line {
    position: absolute;
    top: 652px;
    display: flex;
    align-items: center;
    gap: 12px;
    font-size: 41px;
    letter-spacing: 2px;
  }
  .contact-line--phone { left: 294px; }
  .contact-line--fax { left: 768px; }
  .contact-icon { width: 58px; height: 58px; flex: none; }
</style>
</head>
<body>
<main class="business-card">
  <svg class="tree-artwork" viewBox="0 0 1000 651" role="img" aria-label="Pale blue curling tree illustration with thorny branches behind the contact details">
    <defs>
      <radialGradient id="treeGlow" cx="0.62" cy="0.55" r="0.6">
        <stop offset="0" stop-color="var(--tree-tint)" stop-opacity="0.75"/>
        <stop offset="0.6" stop-color="var(--tree-tint-soft)" stop-opacity="0.55"/>
        <stop offset="1" stop-color="var(--paper)" stop-opacity="0"/>
      </radialGradient>
    </defs>
    <rect width="1000" height="651" fill="url(#treeGlow)"/>
  </svg>

  <div class="brand-name">KVL</div>
  <div class="brand-suffix">Services Ltd</div>

  <address class="address" style="font-style:normal">
    14 Mill Row, Alder Lane,<br>
    Fernbridge, Surrey 7QK
  </address>

  <div class="contact-line contact-line--phone">
    <svg class="contact-icon" viewBox="0 0 58 58" aria-hidden="true">
      <circle cx="29" cy="29" r="27" fill="var(--brand-blue)"/>
      <path d="M20 16c2-1 4 0 5 2l2 5c1 2 0 3-1 4l-2 1c1 4 4 7 8 8l1-2c1-1 2-2 4-1l5 2c2 1 3 3 2 5l-1 2c-2 3-6 3-10 1-7-3-12-8-15-15-2-4-2-8 1-10z" fill="var(--paper)"/>
    </svg>
    <span>020 7946 0318</span>
  </div>

  <div class="contact-line contact-line--fax">
    <svg class="contact-icon" viewBox="0 0 58 58" aria-hidden="true">
      <circle cx="29" cy="29" r="27" fill="var(--brand-blue)"/>
      <rect x="19" y="14" width="20" height="12" fill="var(--paper)"/>
      <rect x="13" y="25" width="32" height="16" rx="3" fill="var(--paper)"/>
      <rect x="19" y="36" width="20" height="9" fill="var(--paper)" stroke="var(--brand-blue)" stroke-width="2"/>
    </svg>
    <span>020 7946 0427</span>
  </div>
</main>
</body>
</html>
```